Quality label design for natural pet care range

Can you create an eye catching label design which will be put onto a range of products?
Initially this is a joint supplement bottle and shampoo for dogs.
We are suppliers of high quality, natural pet supplements and heath care products.
We want to emphasise our brand values, caring, natural and high quality.
Our logo is attached which would need to be included in the design and can be used for colour cues.

The size and specifications have been uploaded to the design brief. Added Monday, January 16, 2017

Reason: There have been some interesting designs but some of the leading ones still need a little refining to meet our needs. I therefore am willing to extend the deadline in order to get exactly what we are looking for. Many thanks

Dog owners in the USA & Canada

Pet Care

• Our logo, barcode and telephone number
• 'Made in the USA' or a stars and stripes flag

```html
<!DOCTYPE html>
<html lang="en">
<head>
<meta charset="utf-8">
<title>Brightpaw Joint Support Label</title>
<link href="https://fonts.googleapis.com/css2?family=Exo+2:wght@700&family=Arimo:wght@700&family=Roboto+Condensed:wght@400&display=swap" rel="stylesheet">
<style>
  :root {
    --backdrop: #dcdcdc;
    --label-white: #f7f8f7;
    --leaf-light: #8cc540;
    --leaf-dark: #1d7a2f;
    --leaf-deep: #16652a;
    --ink: #111111;
    --ink-soft: #2a2a2a;
    --seal-gold: #c9a24a;
    --seal-navy: #1f2a44;
    --photo-warm: #c8742e;
    --photo-light: #e9d8c4;
  }
  html, body {
    margin: 0;
    padding: 0;
    width: 1200px;
    height: 900px;
    overflow: hidden;
    background: var(--backdrop);
  }
  .label {
    position: absolute;
    left: 160px;
    top: 26px;
    width: 880px;
    height: 848px;
    display: block;
  }
  .headline {
    font-family: "Exo 2", sans-serif;
    font-weight: 700;
    font-size: 84px;
    fill: var(--ink);
  }
  .detail {
    font-family: "Arimo", sans-serif;
    font-weight: 700;
    font-size: 29px;
    fill: var(--ink-soft);
    letter-spacing: 0.5px;
  }
  .benefit, .count {
    font-family: "Roboto Condensed", sans-serif;
    font-weight: 400;
    font-size: 36px;
    fill: #ffffff;
  }
  .brand-name {
    font-family: "Arimo", sans-serif;
    font-weight: 700;
    font-size: 34px;
    fill: #ffffff;
  }
</style>
</head>
<body>
<svg class="label" viewBox="0 0 880 848" xmlns="http://www.w3.org/2000/svg">
  <defs>
    <radialGradient id="photoTone" cx="50%" cy="45%" r="60%">
      <stop offset="0%" stop-color="var(--photo-warm)"/>
      <stop offset="100%" stop-color="var(--photo-light)"/>
    </radialGradient>
  </defs>

  <rect class="label-base" x="0" y="0" width="880" height="848" fill="var(--label-white)"/>

  <g class="top-band">
    <path d="M0 0 H880 V180 C700 150 520 100 300 115 C180 122 80 135 0 125 Z" fill="var(--leaf-light)"/>
    <path d="M300 115 C520 100 700 150 880 180 V200 C700 170 520 124 300 132 Z" fill="var(--leaf-dark)"/>
  </g>

  <rect class="hero-photo" x="45" y="100" width="440" height="540" rx="30" fill="url(#photoTone)"
        role="img" aria-label="Photograph of a golden retriever looking forward"/>

  <g class="brand">
    <rect x="568" y="52" width="30" height="30" fill="#ffffff"/>
    <text class="brand-name" x="610" y="80">Brightpaw</text>
  </g>

  <g class="product-title">
    <text class="headline" x="497" y="323">JOINT</text>
    <text class="headline" x="497" y="403">SUPPORT</text>
    <text class="detail" x="499" y="450">Contains Glucosamine,</text>
    <text class="detail" x="499" y="487">Chondroitin and MSM</text>
    <text class="detail" x="499" y="533">Chewable tablets for</text>
    <text class="detail" x="499" y="570">Dogs</text>
  </g>

  <g class="bottom-band">
    <path d="M0 640 C200 600 450 585 880 640 V848 H0 Z" fill="var(--leaf-light)"/>
    <path d="M0 662 C200 625 450 612 880 665 V848 H0 Z" fill="var(--leaf-dark)"/>
  </g>

  <g class="benefits">
    <circle cx="200" cy="683" r="6" fill="#ffffff"/>
    <text class="benefit" x="220" y="695">Connective Issue</text>
    <circle cx="200" cy="728" r="6" fill="#ffffff"/>
    <text class="benefit" x="220" y="740">Maintain Healthy Bones</text>
    <circle cx="200" cy="774" r="6" fill="#ffffff"/>
    <text class="benefit" x="220" y="786">Joint Structure &amp; Function</text>
  </g>

  <g class="quantity">
    <circle cx="302" cy="820" r="26" fill="none" stroke="#ffffff" stroke-width="3"/>
    <text class="count" x="302" y="832" text-anchor="middle">60</text>
    <text class="count" x="340" y="832">Chewables</text>
  </g>

  <g class="quality-seal">
    <circle cx="753" cy="671" r="82" fill="var(--seal-gold)"/>
    <circle cx="753" cy="671" r="64" fill="var(--seal-navy)"/>
  </g>
</svg>
</body>
</html>
```